Saving Lives with Dental Sleep Medicine

Looking for a brochure to market Dental Sleep Medicine educational courses . Whoever wins this bid will be hired to design the rest of our marketing campaign.
Design should be clean, simple with a modern feel. Not busy. Our courses utilize the most modern technology available.
Brochure content is attached, if you can't fit it all that is ok, we can tweak the content later. We are more focused on the look and feel of this design.
This brochure is marketing a 2 day course so there needs to be a spot for date, location, time & cost. As well as a notice of where to register VelmoraLearning.com, info@velmoralearning.com or call 1.800.###.#### and registration fees.
Also need a spot for Dr. Pelloquist's bio (attached). It's too long so just leave as much space as you can and we can amend the content.
Thank you so much. Looking forward to your designs. VelmEd Team :-)
Updates
Hello,
We are hoping for a minimalist design. Not busy. Clean and simple. We can reduce and minimize verbiage as needed. Just looking for layout and design.
Target Market(s)
Dentists
Requirements
Must have
- Clean lines, simple feel, minimalist and modern. Same font as logo. Black, white, gray.
Should not have
- Busy look and feel

```html
<!DOCTYPE html>
<html lang="en">
<head>
<meta charset="utf-8">
<title>Dental Sleep Medicine Education – Brochure</title>
<link href="https://fonts.googleapis.com/css2?family=Crimson+Pro:wght@400;600;700&family=Source+Sans+3:wght@400&display=swap" rel="stylesheet">
<style>
:root{
  --stage:#2c2c2c;
  --cream:#fdf0c8;
  --white:#ffffff;
  --ink:#1d1d1d;
  --slate:#4a4a4c;
  --icon-gray:#d2d2d2;
}
*{margin:0;padding:0;box-sizing:border-box}
html,body{width:1200px;height:1200px;overflow:hidden;background:var(--stage)}
body{position:relative;font-family:"Crimson Pro",Georgia,serif;color:var(--ink)}
.face-label{position:absolute;left:141px;font-family:"Source Sans 3",Arial,sans-serif;font-size:36px;color:#fff;letter-spacing:.5px;line-height:1}
.face{position:absolute;left:139px;width:921px;height:434px;background:var(--white);overflow:hidden}
.back{top:130px}
.inner{top:658px}
.panel{position:absolute;top:0;width:307px;height:434px}
.abs{position:absolute}
.cream{background:var(--cream)}
.brand{display:flex;align-items:center;gap:4px;font-size:9px;font-weight:400;color:var(--ink)}
.brand-square{width:9px;height:9px;background:var(--ink)}
.bio-title{left:48px;top:69px;font-size:10.5px;font-weight:700}
.bio-body{left:48px;top:88px;width:224px;height:330px;font-size:6.9px;line-height:9.25px;overflow:hidden}
.bio-body p{margin-bottom:9px}
.quote-mark{left:56px;top:108px;font-size:30px;font-weight:700;line-height:1}
.quote{left:82px;top:127px;width:200px;font-size:17.4px;line-height:20.5px}
.quote-bar{left:61px;top:254px;width:104px;height:5px;background:var(--ink)}
.contact-title{font-size:13.7px;font-weight:700;line-height:15px}
.contact-line{font-size:11px;line-height:13.7px}
.photo{background:linear-gradient(135deg,#8c8c8c,#3e3e3e 60%,#6b6b6b)}
.title-box{left:14px;top:42px;width:112px;height:61px;background:var(--slate);color:#fff;font-size:14.8px;line-height:18px;padding:2px 0 0 1px}
.brand-box{left:14px;top:15px;width:112px;height:22px;background:#fff;padding-left:3px}
.course-on{left:156px;top:216px;width:145px;font-size:10px;line-height:12.4px}
.course-on strong{font-size:12px;font-weight:700;display:block;line-height:14px}
.detail-title{font-size:13.7px;font-weight:700;line-height:15px}
.detail-line{font-size:11px;line-height:13.7px}
.band{position:absolute;left:0;top:14px;width:921px;height:162px;background:var(--cream)}
.class-photo{left:321px;top:0;width:516px;height:176px;background:linear-gradient(120deg,#8a4a2c,#c9c4bd 45%,#e9e7e2 70%,#6a5a4c)}
.nav{left:759px;top:14px;width:138px;height:59px;background:var(--slate);color:#fff;font-size:9.5px;line-height:15.5px;padding:6px 0 0 10px;letter-spacing:.2px}
.nav span.arrow{position:absolute;left:92px;top:21px;font-size:11px}
.desc-title{left:14px;top:84px;font-size:13px;font-weight:700}
.desc-body{left:14px;top:207px;width:285px;font-size:7.2px;line-height:9.3px}
.desc-body p{margin-bottom:5px}
.program-title{left:371px;top:175px;width:500px;font-size:13.3px;line-height:15px;font-weight:700}
.icon{position:absolute;width:39px;height:39px}
.vbar{position:absolute;width:5px;background:var(--ink)}
.topics{position:absolute;font-size:8.5px;line-height:10.4px;list-style:none}
.topics li{position:relative;padding-left:9px}
.topics li::before{content:"•";position:absolute;left:0}
</style>
</head>
<body>

<div class="face-label" style="top:82px">BACK FACE</div>
<section class="face back">
  <div class="panel cream" style="left:0">
    <div class="abs brand" style="left:15px;top:16px"><span class="brand-square"></span>VelmoraEducation</div>
    <h2 class="abs bio-title">Dr. Pelloquist’s Biography</h2>
    <div class="abs bio-body">
      <p>Dr. Pelloquist received his Doctor of Dental Surgery (DDS) Degree and Bachelor of Medical Sciences from the University of Northvale. He also earned fellowships from International Academy of Restorative Aesthetics &amp; Crestmoor Institute for Advanced Dental Studies. He then furthered his education and training by completing a Research Fellowship in the area of “Sleep and Dental Sleep Medicine” at the Linden University Hospital (LUH), in Antwerp, Belgium.</p>
      <p>Dr. Pelloquist is a general dentist who maintains a group of private practices in Edmonton and Calgary with an interest in Dental Sleep Medicine and TMD Management. He is actively involved in clinical research in Dental Sleep Medicine and his research focuses on developing new technologies to improve treatment outcome predictability and patient selection in Oral Appliance Therapy for patients with OSA (i.e. Obstructive Sleep Apnea) and improving clinical workflow efficiencies, utilizing different digital technologies. He is the recipient of the “2012 &amp; 2015 Clinical Research Award” and “2015 Clinical Excellence Award” from the Continental Academy of Dental Sleep Medicine (CADSM). He has lectured at numerous meetings such as Continental Academy of Sleep Medicine Annual Meeting, CADSM Annual Meeting, GAO (Global Association for Orthodontics) Annual Meeting, Interdisciplinary Coastal Dental Sleep Medicine Academy Annual Meeting (iCDSMA), Northern Society of Dental Sleep Medicine Annual Meeting (NSDSM) and many more Sleep meetings across North America and Europe.</p>
      <p>He is the founder and director of Prairie Dental Sleep Medicine Study Club and the Clinical Director at The Quiet Night Centre in Canada. He is also the Chief Dental Officer at Breezeway Sleep Technologies, the developer of “SOMNx TM” Technology. Dr. Pelloquist is a major advocate for the importance of an inter-disciplinary approach to Dental Sleep Medicine which focuses on the collaboration of Sleep Physicians, Sleep Dentists and other healthcare professionals. He has been treating OSA patients for many years and also has trained hundreds of dentists in Dental Sleep Medicine.</p>
    </div>
  </div>

  <div class="panel" style="left:307px;background:var(--white)">
    <div class="abs quote-mark">“</div>
    <blockquote class="abs quote">Dental clinics should have a comprehensive understanding of sleep and airway disorders and educate their patients.</blockquote>
    <div class="abs quote-bar"></div>
    <div class="abs" style="left:46px;top:357px">
      <div class="contact-title">Contact us</div>
      <div class="contact-line">VelmoraLearning.com</div>
      <div class="contact-line">info@velmoralearning.com</div>
      <div class="contact-line">1.800.###.####</div>
    </div>
  </div>

  <div class="panel cream" style="left:614px">
    <div class="abs photo" style="left:0;top:0;width:307px;height:206px" role="img" aria-label="Black and white portrait of the smiling course instructor in a suit, in an office"></div>
    <div class="abs brand brand-box"><span class="brand-square"></span>VelmoraEducation</div>
    <h1 class="abs title-box" style="font-weight:400">Dental Sleep<br>Medicine<br>Education</h1>
    <div class="abs course-on"><strong>A 2-day course on;</strong>Sleep &amp; Airway Management in a Dental Clinic;<br>SOMNx Plus System &amp; Fully Digital Workflows for OAT</div>
    <div class="abs" style="left:15px;top:299px">
      <div class="detail-title">Course Details</div>
      <div class="detail-line">Date: dd/mm/yyyy</div>
      <div class="detail-line">Location:.....</div>
    </div>
    <div class="abs" style="left:156px;top:313px">
      <div class="detail-line">Time: …….</div>
      <div class="detail-line">Registration fee:....</div>
    </div>
    <div class="abs" style="left:15px;top:354px">
      <div class="contact-title">Contact us</div>
      <div class="contact-line">VelmoraLearning.com</div>
      <div class="contact-line">info@velmoralearning.com</div>
      <div class="contact-line">1.800.###.####</div>
    </div>
  </div>
</section>

<div class="face-label" style="top:608px">INNER FACE</div>
<section class="face inner">
  <div class="band"></div>
  <div class="abs class-photo" role="img" aria-label="Instructor presenting to dentists seated at laptops in a bright training room"></div>
  <nav class="abs nav">BIOGRPAHY<br>OUR WHY<br>COURSE DETAILS<span class="arrow">&gt;&gt;&gt;</span></nav>
  <h2 class="abs desc-title">Course Description</h2>
  <div class="abs brand" style="left:15px;top:184px"><span class="brand-square"></span>VelmoraEducation</div>
  <div class="abs desc-body">
    <p>Dental Sleep Medicine (DSM) has been growing rapidly over the past decade. Despite such growth, Oral Appliance Therapy (OAT) could be challenging in terms of predictability and workflow efficiency, resulting in many clinicians being reluctant to incorporate “Sleep &amp; OAT” into their clinics. However, most of these challenges can now be addressed by utilizing available technologies in healthcare industry; resulting in improved and predictable clinical workflows, patient experience, quality of care and access to care.</p>
    <p>This program will review the importance of Sleep &amp; Airway Management in comprehensive inter-disciplinary treatment planning and how airway &amp; sleep disorders, if left untreated, could adversely impact the long-term prognosis of dental treatments. It will also provide a practical step-by-step guide for implementing a simple &amp; predictable “Sleep and Airway Management” program; utilizing easy to implement systems, improved patient communication &amp; education through Intraoral scanning, &amp; 3D imaging AND a fully digital workflow for OAT.</p>
  </div>
  <div class="abs" style="left:30px;top:358px">
    <div class="contact-title">Contact us</div>
    <div class="contact-line">VelmoraLearning.com</div>
    <div class="contact-line">info@velmoralearning.com</div>
    <div class="contact-line">1.800.###.####</div>
  </div>

  <h2 class="abs program-title">How to implement a sleep and airway management program in a dental clinic and what is involved in helping patients with sleep disorders.</h2>

  <svg class="icon" style="left:370px;top:225px" viewBox="0 0 39 39" aria-hidden="true">
    <rect x="1" y="1" width="37" height="37" rx="4" fill="#fff" stroke="#1d1d1d" stroke-width="1.5"/>
    <rect x="8" y="12" width="2.5" height="16" fill="#1d1d1d"/>
    <rect x="28.5" y="17" width="2.5" height="11" fill="#1d1d1d"/>
    <rect x="8" y="22" width="23" height="2.5" fill="#1d1d1d"/>
    <circle cx="14" cy="18.5" r="2.4" fill="#1d1d1d"/>
    <rect x="17" y="17" width="11" height="4" rx="1" fill="#1d1d1d"/>
  </svg>
  <div class="vbar" style="left:426px;top:225px;height:38px"></div>
  <ul class="topics" style="left:464px;top:223px;width:130px">
    <li>Fundamentals of Sleep &amp; Sleep Disorders</li>
    <li>Understand Obstructive Sleep Apnea (OSA) &amp; Treatment Options</li>
    <li>How to Implement an effective Sleep Screening Protocol in a Dental Clinic</li>
    <li>Sleep Testing</li>
  </ul>

  <svg class="icon" style="left:370px;top:329px" viewBox="0 0 39 39" aria-hidden="true">
    <rect width="39" height="39" fill="var(--icon-gray)"/>
    <circle cx="17" cy="14" r="6" fill="none" stroke="#1d1d1d" stroke-width="1.4"/>
    <path d="M10 14a7 7 0 0 1 14 0" fill="none" stroke="#1d1d1d" stroke-width="1.4"/>
    <path d="M6 34c1-7 5-10 11-10s8 2 9 4" fill="none" stroke="#1d1d1d" stroke-width="1.4"/>
    <path d="M26 36l8-8m0 0l2-3-3 1z" fill="none" stroke="#1d1d1d" stroke-width="1.4"/>
  </svg>
  <div class="vbar" style="left:426px;top:329px;height:40px"></div>
  <ul class="topics" style="left:464px;top:332px;width:150px">
    <li>How to order an appliance for OAT</li>
    <li>Appliance Selection</li>
    <li>Importance of patient selection</li>
    <li>Overview of SOMNx Plus System</li>
  </ul>

  <svg class="icon" style="left:677px;top:230px" viewBox="0 0 39 39" aria-hidden="true">
    <rect x="14" y="2" width="11" height="8" fill="#1d1d1d"/>
    <g fill="#1d1d1d">
      <circle cx="8" cy="20" r="3"/><circle cx="19.5" cy="17" r="3"/><circle cx="31" cy="20" r="3"/>
      <circle cx="5" cy="29" r="3"/><circle cx="15" cy="28" r="3"/><circle cx="24" cy="28" r="3"/><circle cx="34" cy="29" r="3"/>
      <rect x="1" y="32" width="37" height="4" rx="2"/>
    </g>
  </svg>
  <div class="vbar" style="left:733px;top:225px;height:38px"></div>
  <ul class="topics" style="left:770px;top:223px;width:130px">
    <li>Hands-on workshop for SOMNx Tray Fitting</li>
    <li>Hands-on workshop for Bite-Registration</li>
    <li>Technology &amp; Sleep</li>
    <li>Fully Digital Workflow for OAT</li>
  </ul>

  <svg class="icon" style="left:677px;top:325px" viewBox="0 0 39 39" aria-hidden="true">
    <path d="M13 38V4M13 4l-2.5 5h5z M13 24c0 6 3 8 6 8" fill="none" stroke="#1d1d1d" stroke-width="1"/>
  </svg>
  <div class="vbar" style="left:733px;top:329px;height:40px"></div>
  <ul class="topics" style="left:770px;top:327px;width:120px">
    <li>SOMNx Plus Case Studies</li>
    <li>Medical Billing for OAT</li>
    <li>How to maximize the utilization of your SOMNx Plus at your clinic</li>
    <li>Simple and easy to follow clinical workflow</li>
  </ul>
</section>

</body>
</html>
```